Advanced Therapeutic Massage Therapist

I need a business card advertising my massage services as an advanced therapeutic massage therapist. I offer advanced therapeutic massage, swedish and deep tissue. I want to create a simple, professional and feminine card. I like bright colours and creativity.

I prefer a bold and experimental approach rather than something status-quo. A card to suggest therapeutic healing through dynamic massage. Motifs, shapes or layout which suggest movement and flow.
Updates

Target Market(s)

Everybody!

Industry/Entity Type

Health And Wellness

Contact Information for Business Card

The card should include:
My name, logo, services offered and my contact details.

Aoibhín Delaney
Massage Therapist

- Swedish - Deep Tissue - Advanced Therapeutic

Phone: (+353) 87 261 9043
Email: regenerate@aoibhindelaney-example.com
Website: www.aoibhindelany-example.com

Font styles to use
Serif
Sans Serif
Decorative
Script

Colors

Designer to choose colors to be used in the design.

Requirements
Must have
• An example may contain something like this, yet concise:
• "Aoibhín Delaney
• Massage Therapist
• - Swedish - Deep Tissue - Advanced Therapeutic"
Nice to have
• This sentence is optional:
• Imagery such as a logo or symbol. I have attached a file containing a logo I had produced however the name is incorrect now as it is "Aoibhín" not "Evie". It could be edited to change it to Aoibhín.
• I have sent the file as .psd .jpg. .pdf and .png
• I like when the card conveys energy, movement, pressure points, flow etc.
• I just like the designer to follow their own style and ideas. I like bright colours but must have a lot of a base colour to offset it. I really prefer them to follow their own inspiration. That is my preference.
Should not have
• Pine trees, non-native trees to Britain and Ireland, exotic flowers or animals that are not native to Britain and Ireland.
• I don't like brown as the background colour of the card.
• The cars shouldn't look like a wedding invitation i.e too many floral type designs.

```html
<!DOCTYPE html>
<html lang="en">
<head>
<meta charset="UTF-8">
<title>Aoibhín Delaney – Massage Therapist business card</title>
<link href="https://fonts.googleapis.com/css2?family=Cormorant+Garamond:wght@500;600&family=Raleway:wght@400;500&display=swap" rel="stylesheet">
<style>
  :root {
    --stage: #111111;
    --card-white: #ffffff;
    --forest-deep: #1c3a33;
    --forest-mid: #3f6e5c;
    --mist: #e7e4e2;
    --mist-soft: #c9d2cd;
    --copper: #b3531c;
    --gold: #e0a24a;
    --cream: #e9d8b8;
    --ink: #2b2b2b;
    --grey: #6a6a6a;
    --mint: #a9dccb;
    --mint-light: #d4efe6;
  }
  * { margin: 0; padding: 0; box-sizing: border-box; }
  html, body {
    width: 1200px; height: 1000px; overflow: hidden;
    background: var(--stage);
  }
  .canvas {
    position: relative; width: 1200px; height: 1000px;
    display: flex; align-items: center; justify-content: center; gap: 60px;
  }
  .card {
    position: relative; width: 510px; height: 330px;
    border-radius: 22px; overflow: hidden;
  }

  /* Back side */
  .card-back { background: var(--forest-deep); }
  .forest-photo {
    position: absolute; inset: 0 0 90px 0;
    background:
      linear-gradient(180deg, var(--mist) 0%, var(--mist-soft) 35%, rgba(63,110,92,0.85) 70%, var(--forest-deep) 100%),
      linear-gradient(90deg, var(--forest-mid) 0%, transparent 60%);
    background-blend-mode: multiply;
  }
  .contact {
    position: absolute; display: flex; align-items: center; gap: 8px;
    font-family: 'Raleway', sans-serif; font-size: 15px; color: var(--ink);
  }
  .contact svg { width: 14px; height: 14px; fill: var(--copper); }
  .contact-phone { top: 22px; left: 26px; }
  .contact-email { top: 92px; right: 26px; font-size: 16px; }
  .services {
    position: absolute; left: 0; right: 0; bottom: 42px;
    text-align: center;
    font-family: 'Cormorant Garamond', serif; font-weight: 600;
    font-size: 21px; color: var(--cream);
  }
  .tagline {
    position: absolute; left: 0; right: 0; bottom: 20px;
    text-align: center;
    font-family: 'Raleway', sans-serif; font-size: 13px; color: var(--gold);
  }

  /* Front side */
  .card-front {
    background: var(--card-white);
    display: flex; flex-direction: column; align-items: center; justify-content: center;
  }
  .brand-mark {
    width: 130px; height: 130px; border-radius: 50%;
    background: radial-gradient(circle, var(--mint-light) 0%, var(--mint) 100%);
    margin-bottom: 10px;
  }
  .therapist-name {
    font-family: 'Cormorant Garamond', serif; font-weight: 600;
    font-size: 34px; color: var(--copper); line-height: 1;
  }
  .therapist-role {
    font-family: 'Raleway', sans-serif; font-weight: 500;
    font-size: 18px; color: var(--grey); margin-top: 4px;
  }
</style>
</head>
<body>
<main class="canvas">
  <section class="card card-back">
    <div class="forest-photo" role="img" aria-label="Photograph of a misty evergreen forest fading into fog"></div>
    <div class="contact contact-phone">
      <svg viewBox="0 0 24 24" aria-hidden="true"><path d="M6.6 10.8a15.1 15.1 0 0 0 6.6 6.6l2.2-2.2a1 1 0 0 1 1-.25 11.4 11.4 0 0 0 3.6.57 1 1 0 0 1 1 1V20a1 1 0 0 1-1 1A17 17 0 0 1 3 4a1 1 0 0 1 1-1h3.5a1 1 0 0 1 1 1c0 1.25.2 2.45.57 3.57a1 1 0 0 1-.25 1z"/></svg>
      <span>(+353) 87 261 9043</span>
    </div>
    <div class="contact contact-email">
      <svg viewBox="0 0 24 24" aria-hidden="true"><path d="M2 5h20v14H2z M2 5l10 8 10-8" stroke="#fff" stroke-width="1.5"/></svg>
      <span>aoibhinmassage@example.com</span>
    </div>
    <p class="services">Swedish - Deep Tissue - Advanced Therapeutic</p>
    <p class="tagline">HTQA qualified specialising in advanced therapeutic and deep tissue massage</p>
  </section>

  <section class="card card-front">
    <div class="brand-mark" aria-hidden="true"></div>
    <h1 class="therapist-name">Aoibhín Delaney</h1>
    <p class="therapist-role">Massage Therapist</p>
  </section>
</main>
</body>
</html>
```